Ostervik Renovations needs a website.

I need a platform for clients to go and learn about what my company does, see pictures of projects, and contact me about their projects. I am a residential remodeler specializing in general contracting services for kitchens, bathrooms, basements, additions, custom interiors, and more. I have attached my logo to be incorporated.

```html
<!DOCTYPE html>
<html lang="en">
<head>
<meta charset="utf-8">
<title>Ostervik Renovations</title>
<link href="https://fonts.googleapis.com/css2?family=Tenor+Sans&family=Roboto:wght@400;500;700&display=swap" rel="stylesheet">
<style>
:root{
  --green:#1e5b16;
  --green-mid:#2f6e22;
  --green-light:#4a9a2a;
  --hero-a:#3d7d2b;
  --hero-b:#1f5a17;
  --ink:#1a1a1a;
  --text:#333;
  --muted:#c9c9c9;
  --paper:#ffffff;
  --mist:#efefef;
  --dark:#262626;
  --band:#2c2c2c;
}
*{margin:0;padding:0;box-sizing:border-box}
html,body{width:1200px;height:4444px;overflow:hidden}
body{position:relative;background:var(--paper);font-family:"Roboto",Arial,sans-serif;color:var(--text)}
.abs{position:absolute}
.display{font-family:"Tenor Sans",Arial,sans-serif;font-weight:400;letter-spacing:1px}
.center{left:0;width:1200px;text-align:center}
.eyebrow{font-size:14px;font-weight:700;color:var(--green);letter-spacing:.5px}
.photo{position:absolute}

/* header */
.site-header{left:159px;top:0;width:881px;height:98px;background:var(--paper);border-radius:0 0 20px 20px;z-index:5}
.brand-mark{position:absolute;border-radius:50%;border:3px solid var(--green)}
.brand-name{position:absolute;font-family:"Tenor Sans",Arial,sans-serif;color:var(--ink);line-height:1}
.call-icon{left:572px;top:30px;width:40px;height:40px;border-radius:50%;background:var(--green)}
.call-label{left:618px;top:24px;font-size:11px;color:var(--green);letter-spacing:1px}
.call-number{left:618px;top:40px;font-family:"Tenor Sans",Arial,sans-serif;font-size:27px;color:var(--green)}
.menu{left:825px;top:35px;width:22px}
.menu span{display:block;height:3px;background:var(--green);margin-bottom:5px}

/* hero */
.hero{left:0;top:0;width:1200px;height:765px;background:linear-gradient(160deg,var(--hero-a),var(--hero-b))}
.hero-worker{left:180px;top:145px;width:220px;height:535px;background:linear-gradient(180deg,rgba(40,55,45,.55),rgba(20,30,25,.5));border-radius:110px 110px 0 0}
.hero-ring{left:514px;top:178px;width:172px;height:172px;border:4px solid #fff;border-radius:50%}
.hero-welcome{top:386px;font-size:20px;color:#fff}
.hero-title{top:428px;font-size:42px;color:#fff;letter-spacing:3px}
.btn{position:absolute;background:#000;color:#fff;border-radius:30px;font-weight:700;text-align:center}
.hero-btn{left:515px;top:498px;width:170px;height:45px;line-height:45px;font-size:16px}
.tab{position:absolute;left:153px;width:899px;height:86px;background:var(--paper)}
.tab-up{border-radius:36px 36px 0 0}
.tab-down{border-radius:0 0 36px 36px}
.scroll-dot{left:572px;top:650px;width:56px;height:56px;border-radius:50%;background:var(--paper)}

/* about */
.about-label{left:159px;top:835px}
.about-label:after{content:"";display:inline-block;width:165px;height:1px;background:var(--green);margin-left:12px;vertical-align:middle}
.about-title{left:159px;top:860px;font-size:38px;color:var(--green)}
.about-photo{left:159px;top:920px;width:421px;height:182px;border-radius:12px;background:linear-gradient(120deg,#8b6a52,#5a4a3c 60%,#3d3a36)}
.about-text{left:159px;top:1114px;width:430px;font-size:11.5px;line-height:1.65;color:var(--ink)}
.about-btn{left:159px;top:1198px;width:135px;height:36px;line-height:36px;font-size:13px;font-weight:500}
.about-visual{left:605px;top:840px;width:410px;height:410px;border-radius:50%;background:radial-gradient(circle at 50% 40%,#d9d9d9,#9aa89a 70%,#3f6a38)}
.about-person{left:600px;top:960px;width:230px;height:355px;border-radius:115px 115px 0 0;background:linear-gradient(180deg,#7a8d6f,#34506a)}

/* clients band */
.clients{left:0;top:1314px;width:1200px;height:312px;background:linear-gradient(90deg,#3a3a3a,var(--band) 50%,#353535)}
.clients-title{top:1368px;font-size:34px;color:#fff;letter-spacing:2px}
.clients-sub{top:1414px;font-size:21px;color:#fff;letter-spacing:1.5px}
.partner{position:absolute;top:1482px;height:72px;border:2px solid rgba(255,255,255,.55);border-radius:6px}

/* services */
.services{left:0;top:1626px;width:1200px;height:538px;background:var(--mist)}
.services-eyebrow{top:1692px}
.services-title{top:1722px;font-size:38px;color:var(--green)}
.work-photo{position:absolute;top:1783px;width:281px;height:208px;border-radius:6px 6px 0 0}
.work-label{position:absolute;background:var(--paper);border-radius:6px;text-align:center;font-family:"Tenor Sans",Arial,sans-serif;color:var(--ink);box-shadow:0 4px 12px rgba(0,0,0,.06)}
.work-label p{font-family:"Roboto",Arial,sans-serif;font-size:10px;line-height:1.25;color:#555;margin-top:6px}
.play{left:576px;top:1855px;width:45px;height:45px;border-radius:50%;background:rgba(40,40,40,.85)}
.arrow-btn{position:absolute;top:1870px;width:54px;height:54px;border-radius:50%;border:2px solid var(--green);background:var(--paper)}

/* process */
.process{left:0;top:2164px;width:1200px;height:612px;background:linear-gradient(180deg,#dcdcdc,#eeeeee 45%,#d8d8d8)}
.process-eyebrow{top:2230px}
.process-title{top:2259px;font-size:38px;color:var(--green)}
.process-ring{left:480px;top:2366px;width:240px;height:240px;border:7px solid #8a8a8a;border-radius:50%}
.step-num{position:absolute;font-family:"Roboto",Arial,sans-serif;font-weight:700;font-size:58px;color:var(--muted);line-height:1}
.step-photo{position:absolute;width:143px;height:98px;border-radius:8px}
.step-title{position:absolute;font-size:17px;font-weight:700;color:var(--green)}
.step-text{position:absolute;width:200px;font-size:10px;line-height:1.25;color:#444}
.right{text-align:right}

/* testimonials */
.testimonials{left:0;top:2690px;width:1200px;height:866px;background:var(--green)}
.testi-eyebrow{top:2850px;color:#fff}
.testi-title{top:2879px;font-size:36px;color:#fff;letter-spacing:1.5px}
.card{position:absolute;top:2996px;height:300px;background:var(--paper);overflow:hidden}
.card.soft{background:#eef3ec}
.card .quote{position:absolute;top:121px;width:400px;font-size:16px;line-height:1.25;text-align:center;color:var(--ink)}
.card .name{position:absolute;top:226px;width:400px;font-size:19px;font-weight:700;text-align:center;color:var(--ink)}
.card .stars{position:absolute;top:252px;width:400px;font-size:25px;letter-spacing:5px;text-align:center;color:var(--green-light)}
.notch{position:absolute;width:82px;height:76px;background:var(--green);border-radius:18px 0 0 0;color:#fff;font-family:Georgia,serif;font-size:72px;font-weight:700;line-height:100px;text-align:center}
.avatar{position:absolute;top:2952px;width:124px;height:124px;border-radius:50%;border:4px solid #fff;background:linear-gradient(160deg,#c9b6a4,#7c8a78)}
.helmet{left:776px;top:3360px;width:414px;height:196px;border-radius:50% 50% 20% 20%;background:radial-gradient(circle at 40% 40%,#f0c02a,#b58a1a 45%,rgba(60,50,40,.6) 80%,transparent 82%)}

/* contact */
.contact-title{left:159px;top:3660px;font-size:34px;color:var(--ink)}
.field{position:absolute;left:159px;width:432px;height:36px;border:1px solid #bdbdbd;font-size:10px;color:#444;padding:11px 12px}
.submit{left:159px;top:3988px;width:96px;height:38px;line-height:38px;font-size:14px;font-weight:500}
.info-head{position:absolute;left:665px;font-size:11px;font-weight:700;color:var(--ink)}
.info-body{position:absolute;left:665px;font-size:11px;line-height:1.3;color:var(--ink)}
.info-phone{left:665px;top:3846px;font-size:26px;font-weight:700;color:var(--ink);letter-spacing:1px}
.contact-photo{left:890px;top:3690px;width:150px;height:318px;border-radius:75px;background:linear-gradient(180deg,#c9cfd6,#4a5f7d 55%,#2c3a52)}

/* footer */
.footer{left:0;top:4086px;width:1200px;height:358px;background:linear-gradient(180deg,#2e2e2e,#222)}
.foot-head{position:absolute;top:4124px;font-size:20px;color:#fff;border-left:3px solid #fff;padding-left:12px;line-height:22px}
.foot-links{position:absolute;top:4166px;list-style:none;font-size:12px;color:#fff;line-height:18.6px}
.foot-links .more{color:var(--green-light);text-decoration:underline}
.newsletter{left:703px;top:4169px;width:277px;height:31px;border:1px solid #fff;font-size:10px;color:#fff;padding:9px 12px}
.sub-note{left:703px;top:4206px;font-size:8px;color:#ddd}
.social{position:absolute;top:4235px;width:36px;height:36px;border-radius:50%;border:2px solid #fff}
.foot-rule{left:159px;top:4357px;width:794px;border-top:1px dashed #888}
.copyright{top:4386px;font-size:11px;color:#fff}
.foot-ring{left:975px;top:4240px;width:170px;height:170px;border-radius:50%;border:6px solid rgba(255,255,255,.12)}
</style>
</head>
<body>

<!-- hero -->
<div class="abs hero photo" role="img" aria-label="Construction crew working inside a bright renovation site, tinted green"></div>
<div class="abs hero-worker photo" role="img" aria-label="Contractor in a hard hat standing with arms crossed"></div>
<div class="abs hero-ring"></div>
<div class="abs center display hero-welcome">WELCOME TO</div>
<div class="abs center display hero-title">OSTERVIK RENOVATIONS</div>
<div class="btn hero-btn">GET IN TOUCH</div>
<div class="tab tab-up" style="top:679px"></div>
<div class="abs scroll-dot"></div>
<svg class="abs" style="left:589px;top:662px" width="22" height="16" viewBox="0 0 22 16"><path d="M4 4l7 7 7-7" fill="none" stroke="#888" stroke-width="3"/></svg>

<header class="abs site-header">
  <div class="brand-mark" style="left:26px;top:20px;width:56px;height:56px"></div>
  <div class="brand-name" style="left:92px;top:32px;font-size:17px">OSTERVIK<br>RENOVATIONS</div>
  <div class="abs call-icon"></div>
  <svg class="abs" style="left:582px;top:40px" width="20" height="20" viewBox="0 0 24 24"><path d="M6.6 10.8a15 15 0 006.6 6.6l2.2-2.2c.3-.3.7-.4 1-.2 1.1.4 2.3.6 3.6.6.6 0 1 .4 1 1V20c0 .6-.4 1-1 1C10.6 21 3 13.4 3 4c0-.6.4-1 1-1h3.5c.6 0 1 .4 1 1 0 1.3.2 2.5.6 3.6.1.3 0 .7-.2 1z" fill="#fff"/></svg>
  <div class="abs call-label">CALL US</div>
  <div class="abs call-number">1-800 555 0147</div>
  <div class="abs menu"><span></span><span></span><span></span></div>
</header>

<!-- about -->
<div class="abs eyebrow about-label">ABOUT US</div>
<h2 class="abs display about-title">WHAT WE DO</h2>
<div class="abs about-photo photo" role="img" aria-label="Contractor reviewing renovation plans with a couple in their home"></div>
<p class="abs about-text">Lorem ipsum dolor sit amet, consectetur adipiscing elit, sed do eiusmod tempor incididunt ut labore et dolore magna aliqua. Quis ipsum suspendisse ultrices gravida. Risus commodo viverra maecenas accumsan lacus vel facilisis.</p>
<div class="btn about-btn">Learn More</div>
<div class="abs about-visual photo" role="img" aria-label="Round photo of a contractor in a hard hat on site"></div>
<div class="abs about-person photo" role="img" aria-label="Smiling worker in overalls with arms crossed"></div>

<!-- clients -->
<div class="abs clients photo" role="img" aria-label="Dark interior of an empty room under renovation"></div>
<h2 class="abs center display clients-title">500+ CLIENTS WAS TRUST OUR</h2>
<div class="abs center display clients-sub">HOME RENOVATION BUSINESS</div>
<div class="partner" style="left:284px;width:142px"></div>
<div class="partner" style="left:536px;width:116px"></div>
<div class="partner" style="left:776px;width:136px"></div>

<!-- services -->
<div class="abs services"></div>
<div class="abs center eyebrow services-eyebrow">SERVICES</div>
<h2 class="abs center display services-title">OUR WORKS</h2>
<div class="arrow-btn" style="left:68px"></div>
<svg class="abs" style="left:87px;top:1888px" width="16" height="18" viewBox="0 0 16 18"><path d="M11 3L5 9l6 6" fill="none" stroke="#1a1a1a" stroke-width="2.5"/></svg>
<div class="arrow-btn" style="left:1073px"></div>
<svg class="abs" style="left:1093px;top:1888px" width="16" height="18" viewBox="0 0 16 18"><path d="M5 3l6 6-6 6" fill="none" stroke="#1a1a1a" stroke-width="2.5"/></svg>

<div class="work-photo photo" style="left:159px;background:linear-gradient(120deg,#3a3a3a,#8d8d8d 55%,#e6e6e6)" role="img" aria-label="Modern remodeled kitchen with dark cabinets"></div>
<div class="work-label" style="left:176px;top:1967px;width:243px;height:50px;line-height:50px;font-size:21px">Kitchen Remodeling</div>

<div class="work-photo photo" style="left:459px;background:linear-gradient(120deg,#4a4440,#7b736b 50%,#2e2a27)" role="img" aria-label="Renovated bathroom with glass shower"></div>
<div class="abs play"></div>
<svg class="abs" style="left:589px;top:1868px" width="20" height="20" viewBox="0 0 20 20"><path d="M5 15L15 5M8 5h7v7" fill="none" stroke="#fff" stroke-width="2"/></svg>
<div class="work-label" style="left:479px;top:1967px;width:240px;height:107px;padding-top:20px;font-size:21px;color:var(--green)">Bathroom Renovations<p>Lorem ipsum dolor sit amet, consectetur adipiscing elit, sed do eiusmod tempor incididunt ut labore et dolore magna aliqua.</p></div>

<div class="work-photo photo" style="left:759px;background:linear-gradient(120deg,#d8d8d8,#f3f3f3 60%,#c8a070)" role="img" aria-label="Painter finishing a basement wall beside a ladder"></div>
<div class="work-label" style="left:779px;top:1967px;width:243px;height:50px;line-height:50px;font-size:21px">Basement Finishing</div>

<!-- process -->
<div class="abs process photo" role="img" aria-label="Empty bright room with bare concrete walls"></div>
<div class="abs center eyebrow process-eyebrow">OUR RENOVATION PROCCESS</div>
<h2 class="abs center display process-title">HOW IT WORKS</h2>
<div class="tab tab-down" style="top:2690px"></div>
<div class="abs process-ring"></div>

<div class="step-num" style="left:258px;top:2364px">01</div>
<div class="step-photo photo" style="left:336px;top:2341px;background:linear-gradient(120deg,#2e2e2e,#8a7f74 60%,#e2e2e2)" role="img" aria-label="Finished kitchen interior"></div>
<div class="step-title" style="left:264px;top:2446px;width:200px;text-align:right">SMART WORK</div>
<p class="step-text right" style="left:264px;top:2475px">Lorem ipsum dolor sit amet, consectetur adipiscing elit, sed do eiusmod tempor incididunt ut labore et dolore magna aliqua.</p>

<div class="step-photo photo" style="left:755px;top:2436px;background:linear-gradient(120deg,#3f5f8a,#9aa7b3 60%,#d5d5d5)" role="img" aria-label="Worker measuring a wall"></div>
<div class="step-num" style="left:908px;top:2458px">03</div>
<div class="step-title" style="left:762px;top:2547px">BEST IN PRICE</div>
<p class="step-text" style="left:762px;top:2575px">Lorem ipsum dolor sit amet, consectetur adipiscing elit, sed do eiusmod tempor incididunt ut labore et dolore magna aliqua.</p>

<div class="step-title" style="left:294px;top:2654px;width:200px;text-align:right">UNIQUE CONCEPTS</div>
<p class="step-text right" style="left:294px;top:2683px">Lorem ipsum dolor sit amet, consectetur adipiscing elit, sed do eiusmod tempor incididunt ut labore et dolore magna aliqua.</p>
<div class="step-photo photo" style="left:517px;top:2641px;background:linear-gradient(120deg,#f0f0f0,#b9b9b9 55%,#6d7a5e)" role="img" aria-label="Sketch of a planned interior layout"></div>
<div class="step-num" style="left:678px;top:2663px">02</div>

<!-- testimonials -->
<div class="abs testimonials" style="top:2776px;height:780px"></div>
<div class="abs" style="left:0;top:2690px;width:153px;height:86px;background:var(--green)"></div>
<div class="abs" style="left:1052px;top:2690px;width:148px;height:86px;background:var(--green)"></div>
<div class="abs center eyebrow testi-eyebrow">TESTIMONIALS</div>
<h2 class="abs center display testi-title">WHAT OUR CLIENT SAYS</h2>

<div class="card soft" style="left:0;width:343px">
  <p class="quote" style="left:-64px">“Consectetur adipiscing elit. Integer nunc viverra laoreet est the is porta pretium metus aliquam eget maecenas porta is nunc viverra Aenean pulvinar maximus leo ”</p>
  <div class="name" style="left:-64px">Maren</div>
  <div class="stars" style="left:-64px">★★★★★</div>
  <div class="notch" style="left:261px;top:224px">“</div>
</div>
<div class="card" style="left:384px;width:431px">
  <p class="quote" style="left:16px">“Consectetur adipiscing elit. Integer nunc viverra laoreet est the is porta pretium metus aliquam eget maecenas porta is nunc viverra Aenean pulvinar maximus leo ”</p>
  <div class="name" style="left:16px">Sofie</div>
  <div class="stars" style="left:16px">★★★★★</div>
  <div class="notch" style="left:349px;top:224px">“</div>
</div>
<div class="card soft" style="left:858px;width:342px">
  <p class="quote" style="left:14px">“Consectetur adipiscing elit. Integer nunc viverra laoreet est the is porta pretium metus aliquam eget maecenas porta is nunc viverra Aenean pulvinar maximus leo ”</p>
  <div class="name" style="left:14px">Henrik</div>
  <div class="stars" style="left:14px">★★★★★</div>
</div>
<div class="avatar photo" style="left:64px" role="img" aria-label="Portrait of client Maren"></div>
<div class="avatar photo" style="left:538px" role="img" aria-label="Portrait of client Sofie"></div>
<div class="avatar photo" style="left:1010px" role="img" aria-label="Portrait of client Henrik"></div>

<!-- contact -->
<div class="tab tab-up" style="top:3470px;height:90px"></div>
<div class="abs helmet photo" role="img" aria-label="Yellow hard hat with tools on a tool belt"></div>
<div class="brand-mark" style="left:414px;top:3510px;width:100px;height:100px"></div>
<div class="brand-name" style="left:531px;top:3545px;font-size:29px">OSTERVIK<br>RENOVATIONS</div>

<h2 class="abs contact-title display" style="letter-spacing:.5px">Get in Touch</h2>
<div class="field" style="top:3725px">Name*</div>
<div class="field" style="top:3775px">Email*</div>
<div class="field" style="top:3824px">Phone*</div>
<div class="field" style="top:3874px;height:100px">Message*</div>
<div class="btn submit">Submit</div>

<svg class="abs" style="left:639px;top:3733px" width="16" height="20" viewBox="0 0 16 20"><path d="M8 0a7 7 0 00-7 7c0 5 7 13 7 13s7-8 7-13a7 7 0 00-7-7zm0 9.5A2.5 2.5 0 118 4.5a2.5 2.5 0 010 5z" fill="#1e5b16"/></svg>
<div class="info-head" style="top:3733px">Address</div>
<div class="info-body" style="top:3756px">#123, Lorium ipsum dolor<br>city name,<br>NZ 8790</div>
<svg class="abs" style="left:638px;top:3824px" width="18" height="18" viewBox="0 0 24 24"><path d="M6.6 10.8a15 15 0 006.6 6.6l2.2-2.2c.3-.3.7-.4 1-.2 1.1.4 2.3.6 3.6.6.6 0 1 .4 1 1V20c0 .6-.4 1-1 1C10.6 21 3 13.4 3 4c0-.6.4-1 1-1h3.5c.6 0 1 .4 1 1 0 1.3.2 2.5.6 3.6.1.3 0 .7-.2 1z" fill="#1e5b16"/></svg>
<div class="info-head" style="top:3826px">Call Us Anytime</div>
<div class="abs info-phone">1-800 555 0147</div>
<svg class="abs" style="left:638px;top:3896px" width="18" height="14" viewBox="0 0 18 14"><rect width="18" height="14" rx="1" fill="#1e5b16"/><path d="M1 1l8 6 8-6" fill="none" stroke="#fff" stroke-width="1.5"/></svg>
<div class="info-head" style="top:3895px">Email</div>
<div class="info-body" style="top:3922px">info@ostervikrenovations.com</div>
<div class="abs contact-photo photo" role="img" aria-label="Contractor in a hard hat using a power tool"></div>

<!-- footer -->
<footer class="abs footer photo" role="img" aria-label="Dim photo of workers on a construction site"></footer>
<div class="abs foot-ring"></div>
<div class="foot-head" style="left:156px">Quick Links</div>
<ul class="foot-links" style="left:156px"><li>Home</li><li>About Us</li><li>Services</li><li>How it works</li><li>Testimonials</li><li>Contact Us</li></ul>
<div class="foot-head" style="left:451px">Services</div>
<ul class="foot-links" style="left:451px"><li>Kitchen Remodeling</li><li>Bathroom Renovation</li><li>Basement Finishing</li><li>Additions</li><li>Custom interiors</li><li class="more">more</li></ul>
<div class="foot-head" style="left:702px">Newsletter</div>
<div class="abs newsletter">Enter Email id</div>
<svg class="abs" style="left:952px;top:4177px" width="14" height="14" viewBox="0 0 14 14"><path d="M1 7l12-6-4 12-2-5z" fill="#fff"/></svg>
<div class="abs sub-note">Subscribe our newsletter</div>
<div class="social" style="left:703px"></div>
<div class="social" style="left:753px"></div>
<div class="social" style="left:803px"></div>
<div class="social" style="left:853px"></div>
<div class="abs foot-rule"></div>
<div class="abs center copyright">© 2025 | www.ostervikrenovations.com</div>

</body>
</html>
```